Morvane Art

A website showing drawings, thumbnails and full size with space for asize and adescription . With the ability to expand for more pictures and purchase through Quidora online. I already own www.morvaneart.com

```html
<!DOCTYPE html>
<html lang="en">
<head>
<meta charset="utf-8">
<title>Morvane Art</title>
<link href="https://fonts.googleapis.com/css2?family=EB+Garamond:wght@400;500;600;700&display=swap" rel="stylesheet">
<style>
:root{
  --teal:#176b72;
  --teal-deep:#0f5a61;
  --ink:#1d1d1d;
  --grey:#555;
  --price:#3a3f8f;
  --orange:#ee5632;
  --footer:#232323;
  --white:#fff;
}
*{box-sizing:border-box;margin:0;padding:0}
html,body{width:1200px;height:2362px;overflow:hidden;background:#fff}
body{position:relative;font-family:"EB Garamond",Georgia,serif;color:var(--ink)}
.abs{position:absolute}
.top-icons{top:12px;left:940px;display:flex;gap:16px;align-items:center}
.top-icons .sq{width:15px;height:15px;background:#2a76c8;border-radius:2px}
.top-icons .sq.red{background:#e8452c}
.top-icons .sq.sky{background:#1da1f2}
.cart{position:relative}
.cart .badge{position:absolute;top:-6px;right:-7px;width:12px;height:12px;border-radius:50%;background:#111;color:#fff;font-size:9px;line-height:12px;text-align:center;font-family:Arial,sans-serif}
.brand-mark{left:168px;top:50px;width:92px;height:92px;border-radius:50%;background:var(--teal)}
.brand-name{left:0;width:430px;top:174px;text-align:center;font-size:30px;font-weight:500;color:var(--teal);letter-spacing:.5px}
.main-nav{left:0;width:430px;top:232px;text-align:center;list-style:none}
.main-nav li{height:47.5px;font-size:16.5px;letter-spacing:.5px;color:var(--teal)}
.main-nav li.active{color:var(--ink)}
.hero{left:380px;top:38px;width:820px;height:401px;background:#0a0a0a;padding:10px}
.hero-art{width:100%;height:100%;background:linear-gradient(135deg,#6f8a3a 0%,#b07a4f 35%,#5c7d32 60%,#8a3a34 80%,#6aa2c9 100%)}
.thumbs{left:585px;top:355px;display:flex;align-items:center;gap:23px}
.thumb{width:96px;height:58px;border:2px solid #fff;border-radius:4px}
.arrow{color:#fff;font-size:22px;font-family:Arial,sans-serif}
.section-title{left:0;width:1200px;text-align:center;color:var(--teal);font-weight:700}
.rule{height:1px;background:#555}
.gallery-intro{left:200px;width:800px;top:538px;text-align:center;font-size:20px;line-height:32px;color:var(--grey)}
.grid{left:89px;top:623px;display:grid;grid-template-columns:repeat(4,246px);grid-auto-rows:214px;column-gap:13px;row-gap:27px}
.grid div{box-shadow:0 2px 5px rgba(0,0,0,.25)}
.card{width:309px;height:339px;box-shadow:0 2px 6px rgba(0,0,0,.25);overflow:hidden;top:1208px}
.card-art{position:absolute;inset:0}
.card-info{position:absolute;left:0;top:224px;width:248px;height:115px;background:#fff;padding:8px 4px 0 4px}
.card-info h3{font-size:22px;font-weight:500;color:var(--teal);line-height:24px}
.card-info p{font-size:15.5px;line-height:24px;color:var(--grey);margin-top:2px}
.meta{display:flex;align-items:center;margin-top:2px;font-size:15.5px}
.price{color:var(--price);width:105px}
.size{color:var(--grey);margin-right:8px}
.chip{font-size:12px;color:var(--grey);border:1px solid #ddd;padding:1px 3px;margin-right:8px;box-shadow:0 1px 2px rgba(0,0,0,.15)}
.pager{left:579px;top:1593px;display:flex;gap:7px}
.pager span{width:20px;height:20px;border-radius:50%;background:var(--teal);color:#fff;font-size:13px;line-height:20px;text-align:center;font-family:Arial,sans-serif}
.newsletter{left:0;top:1665px;width:1200px;height:327px;background:linear-gradient(120deg,#1a6f78,#23838a 50%,#1d6a86)}
.newsletter h2{position:absolute;top:62px;width:1200px;text-align:center;color:#fff;font-size:42px;font-weight:700;letter-spacing:.5px}
.newsletter p{position:absolute;top:133px;left:300px;width:600px;text-align:center;color:#fff;font-size:15.5px;line-height:26px}
.email{position:absolute;left:330px;top:209px;width:351px;height:47px;border:1px solid #fff;color:#fff;font-size:17px;padding:12px 10px}
.subscribe{position:absolute;left:697px;top:209px;width:170px;height:47px;background:var(--orange);color:#fff;font-size:17px;font-weight:600;text-align:center;line-height:47px}
.site-footer{left:0;top:1992px;width:1200px;height:370px;background:var(--footer);color:#fff}
.foot-mark{left:89px;top:25px;width:82px;height:82px;border-radius:50%;background:#fff}
.foot-brand{left:203px;top:78px;font-size:28px;font-weight:600}
.foot-about{left:89px;top:132px;width:320px;font-size:14px;line-height:26px}
.foot-social{left:89px;top:228px;display:flex;gap:18px;font-size:14px;align-items:center}
.foot-social span::before{content:"";display:inline-block;width:10px;height:10px;background:#fff;margin-right:5px}
.foot-col h4{font-size:22px;font-weight:600;margin-top:78px;margin-bottom:12px}
.foot-col li{list-style:none;font-size:15.5px;line-height:30.5px}
.copyright{left:87px;top:335px;font-size:17px}
.pay{left:1068px;top:330px;font-size:13px;background:#fff;color:var(--ink);padding:2px 6px;border-radius:3px}
</style>
</head>
<body>

<div class="abs top-icons">
  <svg width="16" height="16" viewBox="0 0 16 16" aria-label="Account"><circle cx="8" cy="5" r="4" fill="#176b72"/><path d="M1 16c0-5 14-5 14 0z" fill="#176b72"/></svg>
  <span class="cart"><svg width="18" height="16" viewBox="0 0 18 16" aria-label="Cart"><path d="M0 1h3l2 9h10l2-7H4" fill="none" stroke="#176b72" stroke-width="2"/><circle cx="6" cy="14" r="1.6" fill="#176b72"/><circle cx="14" cy="14" r="1.6" fill="#176b72"/></svg><span class="badge">1</span></span>
  <span class="sq" aria-label="Linkbook"></span>
  <span class="sq red" aria-label="Snapgram"></span>
  <span class="sq sky" aria-label="Chirper"></span>
</div>

<div class="abs brand-mark" aria-hidden="true"></div>
<div class="abs brand-name">MORVANE ART</div>
<ul class="abs main-nav">
  <li class="active">HOME</li><li>ABOUT US</li><li>SHOP</li><li>BLOG</li><li>CONTACT US</li>
</ul>

<div class="abs hero"><div class="hero-art" role="img" aria-label="Featured coloured-pencil drawing of a driver at the wheel seen from above"></div></div>
<div class="abs thumbs">
  <span class="arrow">&#8592;</span>
  <div class="thumb" role="img" aria-label="Thumbnail: diner interior drawing" style="background:linear-gradient(135deg,#7bbf6a,#d9b24b,#8a5ac2)"></div>
  <div class="thumb" role="img" aria-label="Thumbnail: ink sketch of a car" style="background:linear-gradient(135deg,#eee,#777)"></div>
  <div class="thumb" role="img" aria-label="Thumbnail: colourful car drawing" style="background:linear-gradient(135deg,#5aa35a,#e66a2a,#7ab0d8)"></div>
  <span class="arrow">&#8594;</span>
</div>

<div class="abs rule" style="left:309px;top:505px;width:161px"></div>
<div class="abs rule" style="left:711px;top:508px;width:161px"></div>
<h2 class="abs section-title" style="top:478px;font-size:44px">GALLERY</h2>
<p class="abs gallery-intro">Sed ut perspiciatis unde omnis iste natus error sit voluptatem accusantium doloremque laudantium, totam rem aperiam, eaque ipsa</p>

<div class="abs grid">
  <div role="img" aria-label="Drawing of yellow sunglasses with reflections" style="background:linear-gradient(135deg,#f3c21f,#f0a02a 60%,#6e8fd0)"></div>
  <div role="img" aria-label="Drawing of a busy diner interior" style="background:linear-gradient(135deg,#c9c24a,#6fae6a 50%,#9a55c4)"></div>
  <div role="img" aria-label="Drawing of a blue roadster, dark wheels" style="background:linear-gradient(160deg,#3d6a9a,#1a1f2a 60%)"></div>
  <div role="img" aria-label="Drawing of a blue sports car on purple" style="background:linear-gradient(135deg,#8a3aa8,#2f7fc0 50%,#6b3b9a)"></div>
  <div role="img" aria-label="Ink drawing of a black pickup truck" style="background:linear-gradient(135deg,#f4f4f4,#444 60%,#eee)"></div>
  <div role="img" aria-label="Ink drawing of a vintage open car" style="background:linear-gradient(135deg,#bbb,#222 60%,#ddd)"></div>
  <div role="img" aria-label="Drawing of a red sports car" style="background:linear-gradient(160deg,#4a3a9a,#c62a3a 45%,#4a3a8a)"></div>
  <div role="img" aria-label="Drawing of a white truck over water" style="background:linear-gradient(135deg,#e04a4a,#e8eaf0 40%,#3a7ad0)"></div>
</div>

<div class="abs rule" style="left:122px;top:1142px;width:160px"></div>
<div class="abs rule" style="left:914px;top:1142px;width:160px"></div>
<h2 class="abs section-title" style="top:1118px;font-size:40px">MORVANE ART DESCRIPTION</h2>

<article class="abs card" style="left:89px">
  <div class="card-art" role="img" aria-label="Drawing of a green car on red" style="background:linear-gradient(160deg,#e2552a,#5f8a4a 45%,#c9502a)"></div>
  <div class="card-info"><h3>FINIBUS BONORUM</h3><p>Sed ut perspiciatis unde omnis iste natus error sit</p>
    <div class="meta"><span class="price">$88.000</span><span class="size">Size</span><span class="chip">10 inc</span><span class="chip">12 inc</span></div></div>
</article>
<article class="abs card" style="left:445px">
  <div class="card-art" role="img" aria-label="Drawing of a busy diner interior" style="background:linear-gradient(135deg,#e8e6c8,#6fae6a 50%,#9a55c4)"></div>
  <div class="card-info"><h3>FINIBUS BONORUM</h3><p>Sed ut perspiciatis unde omnis iste natus error sit</p>
    <div class="meta"><span class="price">$88.000</span><span class="size">Size</span><span class="chip">10 inc</span><span class="chip">12 inc</span></div></div>
</article>
<article class="abs card" style="left:800px">
  <div class="card-art" role="img" aria-label="Ink drawing of a black pickup truck" style="background:linear-gradient(135deg,#f5f5f5,#333 55%,#eee)"></div>
  <div class="card-info"><h3>FINIBUS BONORUM</h3><p>Sed ut perspiciatis unde omnis iste natus error sit</p>
    <div class="meta"><span class="price">$88.000</span><span class="size">Size</span><span class="chip">10 inc</span><span class="chip">12 inc</span></div></div>
</article>

<div class="abs pager"><span>&#8592;</span><span>&#8594;</span></div>

<section class="abs newsletter">
  <h2>JOIN US&nbsp; NEWSLETTER</h2>
  <p>Sed ut perspiciatis unde omnis iste natus error sit voluptatem accusantium doloremque laudantium, totam rem aperiam</p>
  <div class="email">Enter the email</div>
  <div class="subscribe">SUBSCRIBE</div>
</section>

<footer class="abs site-footer">
  <div class="abs foot-mark" aria-hidden="true"></div>
  <div class="abs foot-brand">MORVANE ART</div>
  <p class="abs foot-about">Sed ut perspiciatis unde omnis iste natus error sit voluptatem accusantium doloremque laudantium, totam rem aperiam, eaque ipsa</p>
  <div class="abs foot-social"><span>Linkbook</span><span>Snapgram</span><span>Chirper</span></div>
  <div class="abs foot-col" style="left:486px;top:0"><h4>Quicks Links</h4><ul><li>Home</li><li>About Us</li><li>Shop</li><li>Blog</li><li>Contact Us</li></ul></div>
  <div class="abs foot-col" style="left:691px;top:0"><h4>Services</h4><ul><li>Lorem ipsum dolor</li><li>Ipsum dolor</li><li>Perspiciatis Unde</li><li>Doloremque</li><li>Laudantium</li></ul></div>
  <div class="abs foot-col" style="left:906px;top:0"><h4>Contact us</h4><ul><li>418 Harlow Lane</li><li>Fenwick Bay, NY 10990</li><li>1 (555) 240-7781</li><li>info@morvaneart.com</li></ul></div>
  <div class="abs copyright">(c) 2019 Morvaneart |&nbsp; All Rights Reserved |&nbsp; Terms and Conditions</div>
  <div class="abs pay">Quidora</div>
</footer>

</body>
</html>
```